Logo and Business card design!

Halvern Estates

We are a Property development and real estate company (needs a logo design).

Halvern estates is based in Sydney Australia and will be dealing with high net worth individuals with a corporate background. The demographic of clients will be relatively youthful and savvy. We do development finance, property development and some portion of property sales

I'd like the 'Halvern' part of the name to be strength of the title, with 'property' playing a very minor part, perhaps in tiny font somewhere off to the bottom or side or something

Thank you!

Target Market(s)

25-55 years old

Industry/Entity Type

Real Estate Development

Contact Information for Business Card

Please arrange this information as you see fit

Doug Pennicott
Managing Director
0417 582 330
doug@halvernestates.com.au
www.halvernestates.com.au

Logo Text

Halvern estates

Font styles to use
Serif

Colors

Designer to choose colors to be used in the design.

Requirements
Must have
• PLEASE VIEW THE UPLOADED IMAGES AND EXAMPLES
• And please put 'property' in small letters at the bottom or to the side. I want it to play a minimalist role, with 'HALVERN' being the feature
• Colours! Please make sure theyre mostly grey and white with possibly some other dark blue and maybe dark grey
Nice to have
• Please feel free to use whatever colors you like, the suggested colors are something I selected momentarily and dont necessarily reflect strict guidelines
Should not have
• NO pictures or shapes of houses. I dont want the logo design to be so literal in its imagery

```html
<!DOCTYPE html>
<html lang="en">
<head>
<meta charset="utf-8">
<title>Halvern Estates – Business Card</title>
<link href="https://fonts.googleapis.com/css2?family=Lato:wght@400;700;900&display=swap" rel="stylesheet">
<style>
  :root {
    --stage: #0c0c0c;
    --card-light: #ffffff;
    --card-dark: #2b2b2b;
    --ink: #3a3a3a;
    --ink-soft: #555555;
    --mark-on-dark: #8e8e8e;
  }
  * { box-sizing: border-box; margin: 0; padding: 0; }
  html, body {
    width: 1200px; height: 1000px; overflow: hidden;
    background: var(--stage);
    font-family: "Lato", Arial, sans-serif;
  }
  .stage { position: relative; width: 1200px; height: 1000px; }
  .card {
    position: absolute;
    width: 500px; height: 286px;
    border-radius: 22px;
    box-shadow: 0 18px 40px rgba(0,0,0,0.6);
  }
  .card--front { left: 70px; top: 300px; background: var(--card-light); color: var(--ink); }
  .card--back { left: 630px; top: 420px; background: var(--card-dark); }

  .brand { display: flex; align-items: center; gap: 12px; }
  .brand__square { width: 26px; height: 26px; background: currentColor; }
  .brand__name {
    font-weight: 900; letter-spacing: 1px; line-height: 1;
  }
  .card--front .brand { position: absolute; left: 34px; top: 34px; color: var(--ink); }
  .card--front .brand__name { font-size: 26px; }
  .card--back .brand { position: absolute; left: 50%; top: 50%; transform: translate(-50%, -50%); color: var(--mark-on-dark); }
  .card--back .brand__square { width: 40px; height: 40px; }
  .card--back .brand__name { font-size: 36px; white-space: nowrap; }

  .contact { position: absolute; left: 200px; top: 126px; }
  .contact__name { font-size: 19px; font-weight: 700; color: var(--ink); }
  .contact__role { font-size: 14px; color: var(--ink-soft); margin-bottom: 12px; }
  .contact__list { list-style: none; }
  .contact__item {
    display: flex; align-items: center; gap: 8px;
    font-size: 14px; color: var(--ink-soft); margin-bottom: 5px;
  }
  .contact__icon { width: 14px; height: 14px; flex: none; }
</style>
</head>
<body>
<main class="stage">
  <section class="card card--front" aria-label="Business card front">
    <div class="brand">
      <span class="brand__square"></span>
      <span class="brand__name">HALVERN ESTATES</span>
    </div>
    <div class="contact">
      <p class="contact__name">Doug Pennicott</p>
      <p class="contact__role">Managing Director</p>
      <ul class="contact__list">
        <li class="contact__item">
          <svg class="contact__icon" viewBox="0 0 14 14" aria-hidden="true">
            <circle cx="7" cy="7" r="7" fill="#3a3a3a"/>
            <path d="M4.5 3.5 L6 3.5 L6.5 5.5 L5.6 6.2 Q6.5 8 7.8 8.4 L8.5 7.5 L10.5 8 L10.5 9.5 Q7 10.5 4.5 6 Z" fill="#fff"/>
          </svg>
          <span>0417 582 330</span>
        </li>
        <li class="contact__item">
          <svg class="contact__icon" viewBox="0 0 14 14" aria-hidden="true">
            <circle cx="7" cy="7" r="7" fill="#3a3a3a"/>
            <rect x="3.5" y="4.5" width="7" height="5" fill="#fff"/>
            <path d="M3.5 4.5 L7 7.3 L10.5 4.5" fill="none" stroke="#3a3a3a" stroke-width="0.8"/>
          </svg>
          <span>doug@halvernestates.com.au</span>
        </li>
        <li class="contact__item">
          <svg class="contact__icon" viewBox="0 0 14 14" aria-hidden="true">
            <circle cx="7" cy="7" r="7" fill="#3a3a3a"/>
            <path d="M7 3 A2.6 2.6 0 0 1 9.6 5.6 Q9.6 7.5 7 11 Q4.4 7.5 4.4 5.6 A2.6 2.6 0 0 1 7 3 Z" fill="#fff"/>
            <circle cx="7" cy="5.6" r="1" fill="#3a3a3a"/>
          </svg>
          <span>www.halvernestates.com.au</span>
        </li>
      </ul>
    </div>
  </section>

  <section class="card card--back" aria-label="Business card back">
    <div class="brand">
      <span class="brand__square"></span>
      <span class="brand__name">HALVERN ESTATES</span>
    </div>
  </section>
</main>
</body>
</html>
```